Natural Health Supplement Company Needs a Product Label Designed

HARVEST ROOT LABS needs a PROBIOTICS product label designed.We are a natural health vitamin and dietary supplement company. Who ever wins will have the opportunity to design a lot more product labels for us.
Product name: PROBIOTICS
*Please use the attached logo and base the label text exactly off the Kelt Wellness label example.
Other product examples have been attached for inspiration.

Colors

Designer to choose colors to be used in the design.

Requirements
Must have
• Product name: PROBIOTICS
• *Please use the attached logo and base the label text exactly off the Kelt Wellness label example.
• Other product examples have been attached for inspiration.

```html
<!DOCTYPE html>
<html lang="en">
<head>
<meta charset="utf-8">
<title>HARVEST ROOT LABS – Probiotics Label</title>
<link href="https://fonts.googleapis.com/css2?family=Arimo:wght@400;700&family=Montserrat:wght@800&family=Nunito:wght@400;800&display=swap" rel="stylesheet">
<style>
  :root {
    --backdrop: #3a92d1;
    --label-white: #ffffff;
    --brand-green: #8cc63f;
    --band-gray: #616161;
    --ink: #1a1a1a;
    --notice-fill: #fdf9c9;
    --capsule-red: #e0352b;
    --capsule-cream: #f6e3c4;
  }
  * { margin: 0; padding: 0; box-sizing: border-box; }
  html, body { width: 1200px; height: 1200px; overflow: hidden; }
  body { background: var(--backdrop); font-family: "Arimo", Arial, sans-serif; color: var(--ink); }

  .label { position: absolute; left: 17px; top: 380px; width: 1168px; height: 440px; background: var(--label-white); }
  .band-top { position: absolute; left: 0; top: 0; width: 100%; height: 24px; background: var(--brand-green); }
  .band-bottom { position: absolute; left: 0; top: 415px; width: 100%; height: 25px; background: var(--band-gray); }

  /* Left panel */
  .directions { position: absolute; left: 23px; top: 31px; font-size: 13.6px; line-height: 15px; white-space: nowrap; }
  .directions p { margin-bottom: 3px; }
  .warnings { font-weight: 700; margin-left: 1px; margin-top: 2px; }
  .fda-notice { position: absolute; left: 23px; top: 231px; height: 51px; background: var(--notice-fill);
    border: 1.6px solid var(--ink); border-radius: 7px; padding: 3px 4px; font-size: 13px; line-height: 15px; white-space: nowrap; }
  .lot-note { position: absolute; left: 26px; top: 291px; font-size: 13px; white-space: nowrap; }
  .potency { position: absolute; left: 26px; top: 309px; font-size: 13px; line-height: 15px; font-weight: 700; white-space: nowrap; }
  .origin { position: absolute; left: 133px; top: 357px; width: 54px; text-align: center; font-size: 8.5px; letter-spacing: 1px; }
  .origin svg { display: block; margin: 2px auto; }
  .recycle-mark { position: absolute; left: 202px; top: 360px; width: 52px; height: 48px; border-radius: 50%; background: var(--brand-green); }

  /* Centre panel */
  .brand { position: absolute; left: 435px; top: 32px; width: 300px; text-align: center; }
  .brand-dot { width: 42px; height: 42px; border-radius: 50%; background: var(--brand-green); margin: 0 auto 10px; }
  .brand-name { font-family: "Nunito", sans-serif; font-weight: 800; font-size: 22px; letter-spacing: 1px; color: var(--brand-green); }
  .product-bar { position: absolute; left: 428px; width: 312px; height: 11px; background: var(--band-gray); border-radius: 3px; }
  .product-bar.upper { top: 182px; }
  .product-bar.lower { top: 242px; }
  .product-name { position: absolute; left: 420px; top: 193px; width: 328px; text-align: center; font-family: "Montserrat", sans-serif;
    font-weight: 800; font-size: 43px; line-height: 48px; color: var(--brand-green); }
  .capsule-art { position: absolute; left: 458px; top: 272px; width: 245px; height: 96px; border-radius: 50%;
    background: radial-gradient(ellipse at center, var(--capsule-red) 0%, #ee8a78 45%, var(--capsule-cream) 70%, rgba(255,255,255,0) 72%); }
  .count { position: absolute; left: 404px; top: 396px; font-size: 17.5px; }

  /* Right panel */
  .facts { position: absolute; left: 790px; top: 28px; width: 346px; height: 292px; border: 1.8px solid var(--ink); border-radius: 12px;
    padding: 2px 8px 0 10px; font-size: 14.6px; }
  .facts-title { font-family: "Nunito", sans-serif; font-weight: 800; font-size: 25px; line-height: 28px; }
  .facts-serving { font-family: "Nunito", sans-serif; font-size: 17px; line-height: 22px; }
  .facts-serving b { font-weight: 800; }
  .rule-thick { height: 5px; background: var(--ink); margin: 1px 0 0 -3px; }
  .rule-thin { height: 1.5px; background: var(--ink); margin-left: -3px; }
  .rule-base { height: 2.5px; margin-top: 6px; }
  .facts-head { font-family: "Nunito", sans-serif; font-weight: 800; font-size: 15px; line-height: 19px; text-align: right; padding-right: 2px; }
  .facts-head span { margin-left: 12px; }
  .facts-row { display: grid; grid-template-columns: 177px 120px 1fr; line-height: 17px; }
  .strain { display: grid; grid-template-columns: 177px 1fr; line-height: 17px; }
  .facts-line { line-height: 17px; }
  .facts-note { margin-top: 8px; line-height: 18px; }
  .other { position: absolute; left: 790px; top: 326px; font-size: 14.3px; line-height: 17.3px; white-space: nowrap; }
  .distributor { position: absolute; left: 820px; top: 362px; width: 340px; text-align: center; font-size: 14.3px; line-height: 17.3px; }
</style>
</head>
<body>
  <section class="label">
    <div class="band-top"></div>

    <div class="directions">
      <p>SUGGESTED USE : As a dietary supplement,take two (2)<br>capsules once daily. For best result, take one (1) capsule<br>during the day and one (1) capsule in the evening. Repeat<br>the process daily. Do not exceed two capsules per day.</p>
      <p>Probiora offers a balanced spectrum of live<br>organisms. Probiora bacteria are critical for healthy<br>digestion, help maintain the integrity of the intestinal lining,<br>support proper intestinal motility and participate in the<br>detoxification process.*</p>
      <p class="warnings">KEEP OUT OF THE REACH OF CHILDREN.<br>DO NOT USE IF SAFETY SEAL IS DAMAGED<br>OR MISSING.<br>STORE IN A COOL, DRY PLACE.</p>
    </div>
    <div class="fda-notice">*These statements have not been evaluated by the<br>Food and Drug Administration. This product is not<br>intended to diagnose, treat cure or prevent any disease.</div>
    <div class="lot-note">Lot # and Expiration Date Printed on bottom of Bottle.</div>
    <div class="potency">This product in formulated with 40 billion CFU per 2 caps<br>and to deliver a minimum potency of 20 billion CFU per<br>2 caps through the best by date.</div>
    <div class="origin">MADE IN
      <svg width="52" height="32" viewBox="0 0 52 32" aria-hidden="true">
        <rect width="52" height="32" fill="#d22630"/>
        <g fill="#fff"><rect y="4.6" width="52" height="2.3"/><rect y="9.2" width="52" height="2.3"/><rect y="13.8" width="52" height="2.3"/><rect y="18.4" width="52" height="2.3"/><rect y="23" width="52" height="2.3"/><rect y="27.6" width="52" height="2.3"/></g>
        <rect width="22" height="16" fill="#2a3a8c"/>
      </svg>U. S. A.</div>
    <div class="recycle-mark" role="img" aria-label="Recycling symbol"></div>

    <div class="brand">
      <div class="brand-dot"></div>
      <div class="brand-name">HARVEST ROOT LABS</div>
    </div>
    <div class="product-bar upper"></div>
    <h1 class="product-name">PROBIOTICS</h1>
    <div class="product-bar lower"></div>
    <div class="capsule-art" role="img" aria-label="Pile of red and cream probiotic capsules"></div>
    <div class="count">60 Capsules</div>

    <div class="facts">
      <div class="facts-title">Supplement Facts</div>
      <div class="facts-serving"><b>Serving Size :</b> 2 Capsules</div>
      <div class="facts-serving"><b>Servings Per Container :</b> 30</div>
      <div class="rule-thick"></div>
      <div class="facts-head">Amount Per Serving<span>%DV</span></div>
      <div class="facts-row"><span>Proprietary Blend</span><span>40 BillionCFU</span><span>**</span></div>
      <div class="facts-line">of Probiotic Bacteria:</div>
      <div class="facts-line">TRAVEXA ® (Bi-Pass Technology)</div>
      <div class="rule-thin"></div>
      <div class="strain"><span>lactobacillus acidophilus</span><span>(La-14)</span></div>
      <div class="strain"><span>Bifidobacterium lactis</span><span>(Bl-04)</span></div>
      <div class="strain"><span>lactobacillus plantarum</span><span>(Lp-115)</span></div>
      <div class="strain"><span>lactobacillus paracasei</span><span>(Lpc - 37)</span></div>
      <div class="facts-line">Marine Polysaccharide Complex</div>
      <div class="facts-line">Fructooligosaccharide</div>
      <div class="rule-thin rule-base"></div>
      <div class="facts-note">**Daily Value (DV) not established</div>
    </div>
    <div class="other"><b>Other Ingredients :</b> Cellulose (Vegetable Capsule),<br>Rice maltodextrin, L-Leucine</div>
    <div class="distributor"><b>Distributed By :</b> Company Name<br>Address, City, ST Zip Code<br>website or phone number</div>

    <div class="band-bottom"></div>
  </section>
</body>
</html>
```